Lorna Tess Tresses Fancy Business Card’s

I want my business cards to be elite, original and very classy. I want the business cards to match the colors of my logo and to match the design posted. I would love the design of the picture I posted

I want the card all white .
The dripping on the top of the card I want it to match the pink color in my logo that’s also posted .
I need my logo on the business card !
I need my Instagram- @lorna.tess.tresses__
And my phone number - 582 907 3365

Target Market(s)

My target market is young woman age 23 to older woman to the age of 65
I want both older and younger women to love my design . I don’t want any cheap looking business cards

Industry/Entity Type

Hair And Beauty

Contact Information for Business Card

Add my logo
Add my Instagram- @lorna.tess.tresses__
My number - 582 907 3365
My website- www.lornatesstresses.example

Font styles to use
Serif
Script

Colors
ffffff
e667a6
e34298

Requirements
Must have
• The business cards must have my logo, my number , my website, and my Instagram!
Nice to have
• Nice to have glitter words that match my logo
• The business cards must look classy and mature
• I want them to be very unique!!
Should not have
• Should not have any colors that doesn’t match my logo ! This is very important! Please

```html
<!DOCTYPE html>
<html lang="en">
<head>
<meta charset="utf-8">
<title>Lorna Tess Tresses – Business Card</title>
<link rel="stylesheet" href="https://fonts.googleapis.com/css2?family=Cinzel:wght@400;600&family=Poppins:wght@400&display=swap">
<style>
  :root {
    --stage: #1c1c1c;
    --card-white: #ffffff;
    --brand-pink: #e34298;
    --soft-pink: #e667a6;
    --ink: #4a4a4a;
    --muted: #8a8a8a;
    --silver-light: #c9c9c9;
    --silver-dark: #7c7c7c;
  }
  * { box-sizing: border-box; margin: 0; padding: 0; }
  html, body { width: 1125px; height: 1200px; overflow: hidden; }
  body { background: var(--stage); position: relative; font-family: "Poppins", sans-serif; }

  .card {
    position: absolute;
    left: 157px;
    width: 826px;
    height: 472px;
    overflow: hidden;
  }
  .card--front { top: 106px; background: var(--card-white); }
  .card--back  { top: 639px; background: var(--brand-pink); }

  .pink-drip {
    position: absolute;
    left: 0;
    top: 0;
    width: 100%;
    height: 70px;
  }

  .brand-name {
    font-family: "Cinzel", serif;
    font-weight: 600;
    text-align: center;
    line-height: 1.1;
    position: absolute;
  }
  .card--front .brand-name {
    color: var(--brand-pink);
    font-size: 40px;
    left: 95px;
    width: 300px;
    top: 245px;
    transform: translateY(-50%);
  }
  .card--back .brand-name {
    color: var(--card-white);
    font-size: 62px;
    left: 0;
    width: 100%;
    top: 50%;
    transform: translateY(-50%);
  }

  .person {
    position: absolute;
    left: 424px;
    top: 124px;
  }
  .person__name {
    font-family: "Cinzel", serif;
    font-weight: 600;
    font-size: 34px;
    color: var(--brand-pink);
    letter-spacing: 1px;
    line-height: 1;
  }
  .person__title {
    font-family: "Cinzel", serif;
    font-weight: 400;
    font-size: 18px;
    color: var(--muted);
    letter-spacing: 1px;
    margin-top: 6px;
  }

  .contacts {
    position: absolute;
    left: 421px;
    top: 212px;
    list-style: none;
  }
  .contacts__item {
    display: flex;
    align-items: center;
    height: 34.5px;
    font-size: 19px;
    color: var(--ink);
  }
  .contacts__icon {
    width: 24px;
    height: 24px;
    margin-right: 8px;
    flex: none;
  }

  .glitter-band {
    position: absolute;
    left: 0;
    bottom: 0;
    width: 100%;
    height: 28px;
    background: linear-gradient(90deg, var(--silver-dark), var(--silver-light) 30%, var(--silver-dark) 55%, var(--silver-light) 80%, var(--silver-dark));
  }
</style>
</head>
<body>

<section class="card card--front" aria-label="Business card front">
  <svg class="pink-drip" viewBox="0 0 826 70" preserveAspectRatio="none" aria-hidden="true">
    <path fill="var(--brand-pink)" d="M0 0H826V14
      C810 14 806 20 806 30 C806 40 796 40 796 30 C796 20 790 16 770 16
      C740 16 735 22 735 44 C735 56 722 56 722 44 C722 24 716 16 690 16
      C650 16 644 20 644 28 C644 36 634 36 634 28 C634 20 620 15 590 15
      C560 15 552 22 552 38 C552 50 540 50 540 38 C540 22 530 16 500 16
      C460 16 452 22 452 52 C452 64 438 64 438 52 C438 24 430 16 400 16
      C360 16 352 20 352 30 C352 40 340 40 340 30 C340 20 330 15 300 15
      C262 15 256 22 256 40 C256 52 244 52 244 40 C244 22 236 16 200 16
      C160 16 152 22 152 30 C152 38 142 38 142 30 C142 20 132 15 100 15
      C66 15 60 22 60 46 C60 58 46 58 46 46 C46 22 38 14 0 14Z"/>
  </svg>

  <div class="brand-name">Lorna Tess<br>Tresses</div>

  <div class="person">
    <div class="person__name">Daniel Reyes</div>
    <div class="person__title">President</div>
  </div>

  <ul class="contacts">
    <li class="contacts__item">
      <svg class="contacts__icon" viewBox="0 0 24 24" aria-hidden="true">
        <circle cx="12" cy="12" r="10.5" fill="none" stroke="var(--brand-pink)" stroke-width="2"/>
        <path d="M8.3 7.2l1.8-.4 1.1 2.6-1.2 1a7 7 0 0 0 3.6 3.6l1-1.2 2.6 1.1-.4 1.8c-4.6.4-8.9-3.9-8.5-8.5z" fill="var(--brand-pink)"/>
      </svg>
      582 907 3365
    </li>
    <li class="contacts__item">
      <svg class="contacts__icon" viewBox="0 0 24 24" aria-hidden="true">
        <circle cx="12" cy="12" r="10.5" fill="none" stroke="var(--brand-pink)" stroke-width="2"/>
        <circle cx="12" cy="12" r="2.3" fill="none" stroke="var(--brand-pink)" stroke-width="1.6"/>
        <path d="M14.3 9.8v3.4c0 1.2 1.8 1.4 2.2 0 .8-3-1.4-5.6-4.5-5.6a4.4 4.4 0 0 0 0 8.8c1 0 1.8-.3 2.5-.8" fill="none" stroke="var(--brand-pink)" stroke-width="1.6" stroke-linecap="round"/>
      </svg>
      @lorna.tess.tresses__
    </li>
    <li class="contacts__item">
      <svg class="contacts__icon" viewBox="0 0 24 24" aria-hidden="true">
        <circle cx="12" cy="12" r="10.5" fill="none" stroke="var(--brand-pink)" stroke-width="2"/>
        <rect x="7" y="8.5" width="10" height="7" fill="var(--brand-pink)"/>
        <path d="M7 8.5l5 4 5-4" fill="none" stroke="var(--card-white)" stroke-width="1"/>
      </svg>
      info@lornatesstresses.example
    </li>
    <li class="contacts__item">
      <svg class="contacts__icon" viewBox="0 0 24 24" aria-hidden="true">
        <circle cx="12" cy="12" r="10.5" fill="none" stroke="var(--brand-pink)" stroke-width="2"/>
        <circle cx="12" cy="12" r="5.5" fill="var(--brand-pink)"/>
        <path d="M6.5 12h11M12 6.5c-2 2.5-2 8.5 0 11M12 6.5c2 2.5 2 8.5 0 11" fill="none" stroke="var(--card-white)" stroke-width="0.9"/>
      </svg>
      www.lornatesstresses.example
    </li>
  </ul>

  <div class="glitter-band" role="img" aria-label="Silver glitter band along the bottom edge"></div>
</section>

<section class="card card--back" aria-label="Business card back">
  <div class="brand-name">Lorna Tess<br>Tresses</div>
</section>

</body>
</html>
```